Reliable and clean label for a natural product!

We would like to have a label design for our CBD SOFT GEL CAPSULES . We are a business family and believe in the power of natural healing. In this label we would like to show a reliable, natural and feminine product mainly.

Font styles to use
Serif
Sans Serif

Colors

Designer to choose colors to be used in the design.

```html
<!DOCTYPE html>
<html lang="en">
<head>
<meta charset="utf-8">
<title>Verdale CBD – CBD Soft Gels Label</title>
<link rel="stylesheet" href="https://fonts.googleapis.com/css2?family=Poppins:wght@300;400&family=Oswald:wght@500&family=Great+Vibes&display=swap">
<style>
  :root {
    --page: #ffffff;
    --label: #f3f1ee;
    --ink: #3b3836;
    --ink-soft: #55514e;
    --muted: #a39d97;
    --taupe: #9b9087;
    --leaf-tint: #e6e2dd;
    --white: #ffffff;
  }
  * { margin: 0; padding: 0; box-sizing: border-box; }
  html, body {
    width: 1200px;
    height: 1200px;
    overflow: hidden;
    background: var(--page);
  }
  .label {
    position: absolute;
    left: 128px;
    top: 82px;
    width: 945px;
    height: 1036px;
    background: var(--label);
    overflow: hidden;
  }
  .leaf-motif {
    position: absolute;
    left: 0;
    top: 364px;
    width: 336px;
    height: 392px;
    background: radial-gradient(ellipse at 45% 55%, var(--leaf-tint) 0%, rgba(230,226,221,0.4) 45%, rgba(243,241,238,0) 72%);
  }
  .centered {
    position: absolute;
    left: 0;
    width: 100%;
    text-align: center;
    white-space: nowrap;
  }
  .brand-mark {
    position: absolute;
    left: 50%;
    top: 58px;
    width: 92px;
    height: 92px;
    margin-left: -46px;
    border: 3px solid var(--ink);
    border-radius: 50%;
  }
  .brand-name {
    top: 170px;
    font-family: 'Poppins', sans-serif;
    font-weight: 400;
    font-size: 50px;
    letter-spacing: 1px;
    color: var(--ink);
  }
  .product-type {
    top: 366px;
    font-family: 'Poppins', sans-serif;
    font-weight: 300;
    font-size: 40px;
    letter-spacing: 1px;
    color: var(--muted);
  }
  .product-name {
    top: 430px;
    font-family: 'Oswald', sans-serif;
    font-weight: 500;
    font-size: 122px;
    line-height: 1.2;
    letter-spacing: 3px;
    background: linear-gradient(180deg, var(--ink-soft) 0%, var(--ink) 60%, #6a6561 100%);
    -webkit-background-clip: text;
    background-clip: text;
    color: transparent;
  }
  .product-form {
    top: 570px;
    font-family: 'Great Vibes', cursive;
    font-size: 96px;
    color: var(--ink);
  }
  .spectrum {
    top: 766px;
    font-family: 'Poppins', sans-serif;
    font-weight: 300;
    font-size: 44px;
    color: var(--muted);
  }
  .divider {
    position: absolute;
    left: 228px;
    top: 840px;
    width: 490px;
    height: 2px;
    background: var(--ink-soft);
  }
  .dosage {
    top: 852px;
    font-family: 'Poppins', sans-serif;
    font-weight: 300;
    font-size: 36px;
    color: var(--ink);
  }
  .count-band {
    position: absolute;
    left: 0;
    top: 938px;
    width: 100%;
    height: 70px;
    background: var(--taupe);
    display: flex;
    align-items: center;
    justify-content: center;
    font-family: 'Poppins', sans-serif;
    font-weight: 400;
    font-size: 38px;
    letter-spacing: 1px;
    color: var(--white);
  }
  .base-rule {
    position: absolute;
    left: 0;
    top: 1022px;
    width: 100%;
    height: 4px;
    background: var(--taupe);
  }
</style>
</head>
<body>
  <section class="label">
    <div class="leaf-motif" role="img" aria-label="Faint outline leaves decoration"></div>

    <div class="brand-mark"></div>
    <div class="centered brand-name">VERDALE CBD</div>

    <div class="centered product-type">RESTORATIVE SUPPLEMENT</div>
    <div class="centered product-name">CBD SOFT GELS</div>
    <div class="centered product-form">Capsules</div>
    <div class="centered spectrum">FULL SPECTRUM</div>
    <div class="divider"></div>
    <div class="centered dosage">25mg cbd per capsule</div>

    <div class="count-band">30 CAPSULES</div>
    <div class="base-rule"></div>
  </section>
</body>
</html>
```